KORVa: AI driven decarbonization application

We are seeking an engaging, user-friendly, and visually appealing user interface for our B2B SaaS platform, Brelmont KORVa. This solution helps large organizations achieve net-zero emissions using AI-driven forecasting, AI models, a emission mitigation library, and a scenario simulator..

A big challenge is to allow the user to work efficiently with multidimensional data.

Requirements:

* Design a modern, professional, and visually striking user interface, catering to a diverse audience within large corporations, including executives, strategists, and environmental specialists.

* Construct an intuitive navigation system, allowing users to seamlessly access functionalities for informed decision-making and tracking progress towards net-zero emissions.

* The application is expected to be used on desktops first

* Incorporate our brand's colors, and visual elements into the design to maintain consistency throughout the application.

* Provide design assets and documentation, such as style guides, design specifications, and necessary assets (e.g., icons, illustrations) for our development team to implement the design. We use Figma and would appreciate delivery as figma files.

Please note that we also need more pages over time. The most important is to get the work bench page right. We will also need:
* a landing page where the users can select previous scenarios and see some high level data.
* A page with information on historical data per asset
* An analytics page
* User and system administration pages.
These pages are out of scope for this project, but they should be available in the navigation solution.

Please submit your initial design concepts, accompanied by a brief explanation of your approach and the rationale behind your design choices. We will offer feedback and collaborate with the chosen designer to refine the design, ensuring it meets our requirements and vision.

We are really hoping to see some elegant user interfaces. The functionality describe in the attachment is important, but the layout is not. Feel free to invent.

Attached files:

Target Market(s)

Energy intensive industries

Requirements
Must have
• Easy to navigate through the different data dimensions: Time, assets, mitigation measures, and advanced details under mitigation measures. The design in the attached files are just our working drafts. Creative alternatives are very welcome.
Nice to have
• Elegant layouts that differ from our working drafts.

```html
<!DOCTYPE html>
<html lang="en">
<head>
<meta charset="utf-8">
<title>Brelmont KORVa – Workbench</title>
<link rel="stylesheet" href="https://fonts.googleapis.com/css2?family=Lexend:wght@400;500&family=Inter:wght@400;500;600&display=swap">
<style>
:root{
  --page:#4a4a4a;
  --nav:#0f5c97;
  --nav-active:#5f9b97;
  --white:#ffffff;
  --card:#f9f9f9;
  --panel:#ececec;
  --ink:#222;
  --muted:#666;
  --pill-blue:#1f5f99;
  --pill-grey:#d6d6d6;
  --teal:#6a9f9c;
  --band:#b9d1ef;
  --area:#93b3e3;
  --bar-teal:#93b4b3;
  --bar-rose:#b87c78;
  --bar-gold:#e0b865;
  --bar-slate:#6f8fb5;
  --bar-lilac:#b8a0c8;
  --bar-brown:#a88c74;
  --bar-grey:#9a9a9a;
  --orange:#e58a63;
  --line-grey:#5e7d8c;
  --line-blue:#4a7fd6;
  --shade:#dcdcf0;
  --now:#e3765a;
}
*{box-sizing:border-box;margin:0;padding:0}
html,body{width:1200px;height:3654px;overflow:hidden;background:var(--page);font-family:Inter,Arial,sans-serif;color:var(--ink)}
.screen{position:absolute;left:48px;width:1090px;height:660px;background:var(--white)}
.sidebar{position:absolute;left:0;top:0;width:183px;height:100%;background:var(--nav);color:var(--white)}
.brand{position:absolute;left:20px;top:14px;font-family:Lexend,sans-serif;font-size:21px;font-weight:400;letter-spacing:1.5px;color:var(--white);display:flex;align-items:center;gap:6px}
.brand i{display:block;width:7px;height:7px;border-radius:50%;background:var(--white)}
.nav-item{position:absolute;left:0;width:100%;padding-left:20px;font-size:9.5px;height:18px;line-height:18px}
.nav-item.group::after{content:"‹";position:absolute;right:10px;font-size:12px}
.nav-sub{position:absolute;left:0;width:100%;padding-left:28px;font-size:7px;height:18px;line-height:18px}
.nav-sub.active{background:var(--nav-active)}
.card{position:absolute;border-radius:6px;border:1px solid #e2e2e2;background:var(--card)}
.measure{left:215px;top:33px;width:425px;height:229px}
.measure.empty{display:flex;align-items:center;justify-content:center;font-family:Lexend,sans-serif;font-size:13px;font-weight:500}
.chart-card{left:661px;top:35px;width:400px;height:234px;background:var(--panel);border:none}
.chart-title{position:absolute;left:38px;top:18px;font-family:Lexend,sans-serif;font-size:13px;font-weight:500}
.chart-dot{position:absolute;left:312px;top:18px;width:9px;height:9px;border-radius:50%;background:#c9d6e6}
.chart-card svg{position:absolute;left:20px;top:46px}
.timeline{position:absolute;left:219px;top:302px;width:841px;height:323px;background:var(--panel);border-radius:6px;overflow:hidden}
.controls{position:absolute;left:16px;top:16px;display:flex;gap:6px}
.controls span{width:18px;height:16px;border-radius:3px;background:var(--white);font-size:8px;display:flex;align-items:center;justify-content:center}
.controls span.play{background:var(--teal);color:var(--white)}
.axis{position:absolute;left:0;top:0}
.tl-label{position:absolute;top:13px;font-size:6.5px;transform:translateX(-50%);white-space:nowrap}
.cursor{position:absolute;top:31px;width:2px;background:var(--teal)}
.cursor.now{background:var(--now)}
.mini{position:absolute;left:0;top:260px}
.row{position:absolute;left:174px;right:8px;background:#dedede}
.bar{position:absolute;color:var(--white);font-size:8px;padding:4px 10px;line-height:1.2}
.bar small{display:block;font-size:4.5px;opacity:.9}
.bar .info{position:absolute;right:10px;top:50%;transform:translateY(-50%);width:9px;height:9px;border-radius:50%;background:var(--white);color:var(--ink);font-size:6px;text-align:center;line-height:9px}
.field{position:absolute;height:20px;color:var(--white);font-size:9px;line-height:20px;padding-left:10px}
.band{position:absolute;left:0;right:0;background:var(--band)}
.dt-title{position:absolute;left:0;right:0;top:14px;text-align:center;font-family:Lexend,sans-serif;font-size:11px}
.dt-h{position:absolute;top:43px;font-family:Lexend,sans-serif;font-size:9px}
.filters{position:absolute;left:12px;top:70px;display:flex;gap:4px;align-items:center;font-size:6.5px}
.filters b{font-weight:500;margin-right:6px}
.pill{display:inline-block;background:var(--pill-blue);color:var(--white);border-radius:7px;padding:2px 9px;font-size:4.5px}
.assets{position:absolute;left:12px;top:94px;border-collapse:collapse;font-size:5.5px}
.assets td{height:18.5px;padding-right:15px;font-weight:500}
.params{position:absolute;left:283px;top:68px;font-size:6.5px}
.params div{display:flex;justify-content:space-between;width:110px;height:23.5px;align-items:flex-start}
.params span.pv{background:var(--pill-grey);border-radius:6px;width:48px;text-align:center;font-size:4.5px;padding:2px 0}
</style>
</head>
<body>

<!-- ===== Screen 1 ===== -->
<section class="screen" style="top:52px">
  <nav class="sidebar">
    <div class="brand">BRELMONT<i></i></div>
    <div class="nav-item" style="top:63px">Switch Energy Carrier</div>
    <div class="nav-item group" style="top:90px">Energy Efficiency Measures</div>
    <div class="nav-sub" style="top:124px">Switch Energy Carrier</div>
    <div class="nav-sub" style="top:147px">Energy Efficiency Measures</div>
    <div class="nav-sub" style="top:170px">Venting To Flare</div>
    <div class="nav-sub" style="top:194px">Venting To Production</div>
    <div class="nav-sub" style="top:217px">Fugitive Emissions Measure</div>
    <div class="nav-sub" style="top:240px">Compressor Replacement</div>
    <div class="nav-sub" style="top:264px">Reduced Water Injection</div>
    <div class="nav-sub" style="top:287px">Drilling Improvements</div>
    <div class="nav-item group" style="top:319px">Ending Of Pipe Measures</div>
    <div class="nav-item group" style="top:345px">Company Structure</div>
    <div class="nav-sub" style="top:374px">Change End Of Life</div>
    <div class="nav-sub" style="top:400px">New Net Zero Assets</div>
    <div class="nav-sub" style="top:426px">Update License OwnerShips</div>
  </nav>
  <div class="card measure empty">Select A Mitigation Measure</div>
  <div class="card chart-card">
    <div class="chart-title">Predicted Specific CO2 Emissions</div><div class="chart-dot"></div>
    <svg width="320" height="170" viewBox="0 0 320 170" font-size="4.5" fill="#888">
      <rect x="40" y="5" width="120" height="140" fill="var(--shade)"/>
      <g><text x="22" y="8">175</text><text x="22" y="28">150</text><text x="22" y="48">125</text><text x="22" y="68">100</text><text x="26" y="88">75</text><text x="26" y="108">50</text><text x="26" y="128">25</text><text x="30" y="146">0</text></g>
      <polyline fill="none" stroke="var(--orange)" stroke-width="1" points="40,125 44,112 47,128 50,118 53,122 56,108 59,124 62,115 65,118 68,100 71,112 74,106 77,114 80,96 83,104 86,92 89,108 92,88 95,100 98,80 101,96 104,84 107,94 110,60 113,90 116,72 119,92 122,50 125,85 128,70 131,88 134,75 137,90 140,78 143,86 146,80 150,88 155,82 160,86"/>
      <polyline fill="none" stroke="var(--orange)" stroke-width=".8" points="160,86 185,78 205,72 215,65 225,66 230,58 240,56 245,48 255,44 260,38 270,34 275,28 285,24 290,18 296,14"/>
      <polyline fill="none" stroke="var(--line-grey)" stroke-width=".8" points="160,86 195,110 230,122 260,130 296,140"/>
      <g fill="#888"><text x="40" y="156">1995</text><text x="64" y="156">2000</text><text x="88" y="156">2005</text><text x="112" y="156">2010</text><text x="136" y="156">2015</text><text x="160" y="156">2020</text><text x="184" y="156">2025</text><text x="208" y="156">2030</text><text x="232" y="156">2035</text><text x="256" y="156">2040</text><text x="280" y="156">2045</text></g>
      <line x1="110" y1="165" x2="118" y2="165" stroke="var(--orange)"/><text x="120" y="167">Average</text>
      <line x1="150" y1="165" x2="158" y2="165" stroke="var(--line-grey)"/><text x="160" y="167">Goals</text>
    </svg>
  </div>
  <div class="timeline">
    <div class="controls"><span>«</span><span class="play">▶</span><span>»</span></div>
    <svg class="axis" width="841" height="40">
      <defs><pattern id="tk1" width="6" height="6" patternUnits="userSpaceOnUse"><line x1="0.5" y1="0" x2="0.5" y2="6" stroke="#555" stroke-width=".6"/></pattern></defs>
      <line x1="116" y1="31" x2="841" y2="31" stroke="#333" stroke-width="1"/>
      <rect x="116" y="25" width="725" height="6" fill="url(#tk1)"/>
    </svg>
    <span class="tl-label" style="left:173px">January 2023</span><span class="tl-label" style="left:288px">July 2023</span><span class="tl-label" style="left:420px">January 2023</span><span class="tl-label" style="left:536px">July 2023</span><span class="tl-label" style="left:658px">January 2023</span><span class="tl-label" style="left:783px">July 2023</span>
    <div class="cursor" style="left:172px;height:260px"></div>
    <svg class="mini" width="841" height="63">
      <rect x="241" y="0" width="247" height="63" fill="var(--band)"/>
      <path d="M0,47 L40,44 L80,45 L120,40 L160,43 L200,38 L241,41 L260,30 L280,34 L300,28 L330,33 L360,27 L390,32 L420,28 L450,31 L488,36 L530,44 L570,40 L610,44 L650,39 L690,43 L730,38 L770,42 L810,40 L841,42 L841,63 L0,63Z" fill="var(--area)"/>
    </svg>
  </div>
</section>

<!-- ===== Screen 2 ===== -->
<section class="screen" style="top:770px">
  <nav class="sidebar">
    <div class="brand">BRELMONT<i></i></div>
    <div class="nav-item" style="top:63px">Switch Energy Carrier</div>
    <div class="nav-item group" style="top:90px">Energy Efficiency Measures</div>
    <div class="nav-sub" style="top:124px">Switch Energy Carrier</div>
    <div class="nav-sub" style="top:147px">Energy Efficiency Measures</div>
    <div class="nav-sub" style="top:170px">Venting To Flare</div>
    <div class="nav-sub" style="top:194px">Venting To Production</div>
    <div class="nav-sub" style="top:217px">Fugitive Emissions Measure</div>
    <div class="nav-sub active" style="top:240px">Compressor Replacement</div>
    <div class="nav-sub" style="top:264px">Reduced Water Injection</div>
    <div class="nav-sub" style="top:287px">Drilling Improvements</div>
    <div class="nav-item group" style="top:319px">Ending Of Pipe Measures</div>
    <div class="nav-item group" style="top:345px">Company Structure</div>
    <div class="nav-sub" style="top:374px">Change End Of Life</div>
    <div class="nav-sub" style="top:400px">New Net Zero Assets</div>
    <div class="nav-sub" style="top:426px">Update License OwnerShips</div>
  </nav>
  <div class="card measure">
    <div class="dt-title">Compressor rebundling</div>
    <div class="dt-h" style="left:103px">Assets</div><div class="dt-h" style="left:305px">Prameters</div>
    <div class="filters"><b>Active filters</b><span class="pill">Lorem ipsum</span><span class="pill">Lorem ipsum</span><span class="pill">Lorem ipsum</span></div>
    <table class="assets">
      <tr><td>Lorem Ipsum</td><td>Lorem</td><td>Lorem</td><td>Lorem Ipsum</td><td>100%</td><td>Lorem</td></tr>
      <tr><td>Lorem Ipsum</td><td>Lorem</td><td>Lorem</td><td>Lorem Ipsum</td><td>100%</td><td>Lorem</td></tr>
      <tr><td>Lorem Ipsum</td><td>Lorem</td><td>Lorem</td><td>Lorem Ipsum</td><td>100%</td><td>Lorem</td></tr>
      <tr><td>Lorem Ipsum</td><td>Lorem</td><td>Lorem</td><td>Lorem Ipsum</td><td>100%</td><td>Lorem</td></tr>
      <tr><td>Lorem Ipsum</td><td>Lorem</td><td>Lorem</td><td>Lorem Ipsum</td><td>100%</td><td>Lorem</td></tr>
      <tr><td>Lorem Ipsum</td><td>Lorem</td><td>Lorem</td><td>Lorem Ipsum</td><td>100%</td><td>Lorem</td></tr>
      <tr><td>Lorem Ipsum</td><td>Lorem</td><td>Lorem</td><td>Lorem Ipsum</td><td>100%</td><td>Lorem</td></tr>
    </table>
    <div class="params">
      <div><span>Start</span><span class="pv">January 2023</span></div>
      <div><span>End</span><span class="pv">October 2024</span></div>
      <div><span>Duration</span><span class="pv">21 Months</span></div>
      <div><span>Factor</span><span class="pv">2x</span></div>
      <div><span>Jalla Jalla</span><span class="pv">2x</span></div>
    </div>
  </div>
  <div class="card chart-card">
    <div class="chart-title">Predicted Specific CO2 Emissions</div><div class="chart-dot"></div>
    <svg width="320" height="170" viewBox="0 0 320 170" font-size="4.5" fill="#888">
      <rect x="40" y="5" width="120" height="140" fill="var(--shade)"/>
      <g><text x="22" y="8">175</text><text x="22" y="28">150</text><text x="22" y="48">125</text><text x="22" y="68">100</text><text x="26" y="88">75</text><text x="26" y="108">50</text><text x="26" y="128">25</text><text x="30" y="146">0</text></g>
      <polyline fill="none" stroke="var(--orange)" stroke-width="1" points="40,125 44,112 47,128 50,118 53,122 56,108 59,124 62,115 65,118 68,100 71,112 74,106 77,114 80,96 83,104 86,92 89,108 92,88 95,100 98,80 101,96 104,84 107,94 110,60 113,90 116,72 119,92 122,50 125,85 128,70 131,88 134,75 137,90 140,78 143,86 146,80 150,88 155,82 160,86"/>
      <polyline fill="none" stroke="var(--orange)" stroke-width=".8" points="160,86 185,78 205,72 215,65 225,66 230,58 240,56 245,48 255,44 260,38 270,34 275,28 285,24 290,18 296,14"/>
      <polyline fill="none" stroke="var(--line-grey)" stroke-width=".8" points="160,86 195,110 230,122 260,130 296,140"/>
      <g><text x="40" y="156">1995</text><text x="64" y="156">2000</text><text x="88" y="156">2005</text><text x="112" y="156">2010</text><text x="136" y="156">2015</text><text x="160" y="156">2020</text><text x="184" y="156">2025</text><text x="208" y="156">2030</text><text x="232" y="156">2035</text><text x="256" y="156">2040</text><text x="280" y="156">2045</text></g>
      <line x1="110" y1="165" x2="118" y2="165" stroke="var(--orange)"/><text x="120" y="167">Average</text>
      <line x1="150" y1="165" x2="158" y2="165" stroke="var(--line-grey)"/><text x="160" y="167">Goals</text>
    </svg>
  </div>
  <div class="timeline">
    <div class="controls"><span>«</span><span class="play">▶</span><span>»</span></div>
    <svg class="axis" width="841" height="40">
      <defs><pattern id="tk2" width="6" height="6" patternUnits="userSpaceOnUse"><line x1="0.5" y1="0" x2="0.5" y2="6" stroke="#555" stroke-width=".6"/></pattern></defs>
      <line x1="116" y1="31" x2="841" y2="31" stroke="#333"/>
      <rect x="116" y="25" width="725" height="6" fill="url(#tk2)"/>
    </svg>
    <span class="tl-label" style="left:173px">January 2023</span><span class="tl-label" style="left:288px">July 2023</span><span class="tl-label" style="left:420px">January 2023</span><span class="tl-label" style="left:536px">July 2023</span><span class="tl-label" style="left:658px">January 2023</span><span class="tl-label" style="left:783px">July 2023</span>
    <div class="cursor" style="left:172px;height:260px"></div>
    <svg class="mini" width="841" height="63">
      <rect x="241" y="0" width="247" height="63" fill="var(--band)"/>
      <path d="M0,47 L40,44 L80,45 L120,40 L160,43 L200,38 L241,41 L260,30 L280,34 L300,28 L330,33 L360,27 L390,32 L420,28 L450,31 L488,36 L530,44 L570,40 L610,44 L650,39 L690,43 L730,38 L770,42 L810,40 L841,42 L841,63 L0,63Z" fill="var(--area)"/>
    </svg>
  </div>
</section>

<!-- ===== Screen 3 ===== -->
<section class="screen" style="top:1488px">
  <nav class="sidebar">
    <div class="brand">BRELMONT<i></i></div>
    <div class="nav-item" style="top:63px">Switch Energy Carrier</div>
    <div class="nav-item group" style="top:90px">Energy Efficiency Measures</div>
    <div class="nav-sub" style="top:124px">Switch Energy Carrier</div>
    <div class="nav-sub" style="top:147px">Energy Efficiency Measures</div>
    <div class="nav-sub" style="top:170px">Venting To Flare</div>
    <div class="nav-sub" style="top:194px">Venting To Production</div>
    <div class="nav-sub" style="top:217px">Fugitive Emissions Measure</div>
    <div class="nav-sub" style="top:240px">Compressor Replacement</div>
    <div class="nav-sub" style="top:264px">Reduced Water Injection</div>
    <div class="nav-sub" style="top:287px">Drilling Improvements</div>
    <div class="nav-item group" style="top:319px">Ending Of Pipe Measures</div>
    <div class="nav-item group" style="top:345px">Company Structure</div>
    <div class="nav-sub" style="top:374px">Change End Of Life</div>
    <div class="nav-sub" style="top:400px">New Net Zero Assets</div>
    <div class="nav-sub" style="top:426px">Update License OwnerShips</div>
  </nav>
  <div class="card measure">
    <div class="dt-title">Compressor rebundling</div>
    <div class="dt-h" style="left:103px">Assets</div><div class="dt-h" style="left:305px">Prameters</div>
    <div class="filters"><b>Active filters</b><span class="pill">Lorem ipsum</span><span class="pill">Lorem ipsum</span><span class="pill">Lorem ipsum</span></div>
    <table class="assets">
      <tr><td>Lorem Ipsum</td><td>Lorem</td><td>Lorem</td><td>Lorem Ipsum</td><td>100%</td><td>Lorem</td></tr>
      <tr><td>Lorem Ipsum</td><td>Lorem</td><td>Lorem</td><td>Lorem Ipsum</td><td>100%</td><td>Lorem</td></tr>
      <tr><td>Lorem Ipsum</td><td>Lorem</td><td>Lorem</td><td>Lorem Ipsum</td><td>100%</td><td>Lorem</td></tr>
      <tr><td>Lorem Ipsum</td><td>Lorem</td><td>Lorem</td><td>Lorem Ipsum</td><td>100%</td><td>Lorem</td></tr>
      <tr><td>Lorem Ipsum</td><td>Lorem</td><td>Lorem</td><td>Lorem Ipsum</td><td>100%</td><td>Lorem</td></tr>
      <tr><td>Lorem Ipsum</td><td>Lorem</td><td>Lorem</td><td>Lorem Ipsum</td><td>100%</td><td>Lorem</td></tr>
      <tr><td>Lorem Ipsum</td><td>Lorem</td><td>Lorem</td><td>Lorem Ipsum</td><td>100%</td><td>Lorem</td></tr>
    </table>
    <div class="params">
      <div><span>Start</span><span class="pv">January 2023</span></div>
      <div><span>End</span><span class="pv">October 2024</span></div>
      <div><span>Duration</span><span class="pv">21 Months</span></div>
      <div><span>Factor</span><span class="pv">2x</span></div>
      <div><span>Jalla Jalla</span><span class="pv">2x</span></div>
    </div>
  </div>
  <div class="card chart-card">
    <div class="chart-title">Predicted Specific CO2 Emissions</div><div class="chart-dot"></div>
    <svg width="320" height="170" viewBox="0 0 320 170" font-size="4.5" fill="#888">
      <rect x="40" y="5" width="120" height="140" fill="var(--shade)"/>
      <g><text x="22" y="8">175</text><text x="22" y="28">150</text><text x="22" y="48">125</text><text x="22" y="68">100</text><text x="26" y="88">75</text><text x="26" y="108">50</text><text x="26" y="128">25</text><text x="30" y="146">0</text></g>
      <polyline fill="none" stroke="var(--orange)" stroke-width="1" points="40,125 44,112 47,128 50,118 53,122 56,108 59,124 62,115 65,118 68,100 71,112 74,106 77,114 80,96 83,104 86,92 89,108 92,88 95,100 98,80 101,96 104,84 107,94 110,60 113,90 116,72 119,92 122,50 125,85 128,70 131,88 134,75 137,90 140,78 143,86 146,80 150,88 155,82 160,86"/>
      <polyline fill="none" stroke="var(--orange)" stroke-width=".8" points="160,86 185,78 205,72 215,65 225,66 230,58 240,56 245,48 255,44 260,38 270,34 275,28 285,24 290,18 296,14"/>
      <polyline fill="none" stroke="var(--line-grey)" stroke-width=".8" points="160,86 195,110 230,122 260,130 296,140"/>
      <polyline fill="none" stroke="var(--line-blue)" stroke-width=".8" points="160,86 170,96 176,92 184,102 190,98 198,106 204,102 212,110 220,105 228,112 236,108 244,114 252,110 262,116 272,113 282,118 296,116"/>
      <g><text x="40" y="156">1995</text><text x="64" y="156">2000</text><text x="88" y="156">2005</text><text x="112" y="156">2010</text><text x="136" y="156">2015</text><text x="160" y="156">2020</text><text x="184" y="156">2025</text><text x="208" y="156">2030</text><text x="232" y="156">2035</text><text x="256" y="156">2040</text><text x="280" y="156">2045</text></g>
      <line x1="90" y1="165" x2="98" y2="165" stroke="var(--orange)"/><text x="100" y="167">Average</text>
      <line x1="135" y1="165" x2="143" y2="165" stroke="var(--line-grey)"/><text x="145" y="167">Goals</text>
      <line x1="175" y1="165" x2="183" y2="165" stroke="var(--line-blue)"/><text x="185" y="167">With measure</text>
    </svg>
  </div>
  <div class="timeline">
    <div class="controls"><span>«</span><span class="play">▶</span><span>»</span></div>
    <svg class="axis" width="841" height="40">
      <defs><pattern id="tk3" width="6" height="6" patternUnits="userSpaceOnUse"><line x1="0.5" y1="0" x2="0.5" y2="6" stroke="#555" stroke-width=".6"/></pattern></defs>
      <line x1="116" y1="31" x2="841" y2="31" stroke="#333"/>
      <rect x="116" y="25" width="725" height="6" fill="url(#tk3)"/>
    </svg>
    <span class="tl-label" style="left:173px">January 2023</span><span class="tl-label" style="left:288px">July 2023</span><span class="tl-label" style="left:420px">January 2023</span><span class="tl-label" style="left:536px">July 2023</span><span class="tl-label" style="left:658px">January 2023</span><span class="tl-label" style="left:783px">July 2023</span>
    <div class="band" style="top:139px;height:40px"></div>
    <div class="bar" style="left:206px;top:139px;width:202px;height:40px;background:var(--bar-teal);padding-top:10px">Compressor rebundling<small>Lorem ipsum dolor sit amet</small><span class="info">i</span></div>
    <svg class="mini" width="841" height="63">
      <rect x="241" y="0" width="247" height="63" fill="var(--band)"/>
      <path d="M0,47 L40,44 L80,45 L120,40 L160,43 L200,38 L241,41 L260,30 L280,34 L300,28 L330,33 L360,27 L390,32 L420,28 L450,31 L488,36 L530,44 L570,40 L610,44 L650,39 L690,43 L730,38 L770,42 L810,40 L841,42 L841,63 L0,63Z" fill="var(--area)"/>
    </svg>
  </div>
</section>

<!-- ===== Screen 4 ===== -->
<section class="screen" style="top:2206px">
  <nav class="sidebar">
    <div class="brand">BRELMONT<i></i></div>
    <div class="nav-item" style="top:63px">Switch Energy Carrier</div>
    <div class="nav-item group" style="top:90px">Energy Efficiency Measures</div>
    <div class="nav-sub" style="top:124px">Switch Energy Carrier</div>
    <div class="nav-sub" style="top:147px">Energy Efficiency Measures</div>
    <div class="nav-sub" style="top:170px">Venting To Flare</div>
    <div class="nav-sub" style="top:194px">Venting To Production</div>
    <div class="nav-sub" style="top:217px">Fugitive Emissions Measure</div>
    <div class="nav-sub" style="top:240px">Compressor Replacement</div>
    <div class="nav-sub" style="top:264px">Reduced Water Injection</div>
    <div class="nav-sub" style="top:287px">Drilling Improvements</div>
    <div class="nav-item group" style="top:319px">Ending Of Pipe Measures</div>
    <div class="nav-item group" style="top:345px">Company Structure</div>
    <div class="nav-sub" style="top:374px">Change End Of Life</div>
    <div class="nav-sub" style="top:400px">New Net Zero Assets</div>
    <div class="nav-sub" style="top:426px">Update License OwnerShips</div>
  </nav>
  <div class="card measure empty" style="left:219px">Select A Mitigation Measure</div>
  <div class="card chart-card">
    <div class="chart-title">Predicted Specific CO2 Emissions</div><div class="chart-dot"></div>
    <svg width="320" height="170" viewBox="0 0 320 170" font-size="4.5" fill="#888">
      <rect x="40" y="5" width="120" height="140" fill="var(--shade)"/>
      <g><text x="22" y="8">175</text><text x="22" y="28">150</text><text x="22" y="48">125</text><text x="22" y="68">100</text><text x="26" y="88">75</text><text x="26" y="108">50</text><text x="26" y="128">25</text><text x="30" y="146">0</text></g>
      <polyline fill="none" stroke="var(--orange)" stroke-width="1" points="40,125 44,112 47,128 50,118 53,122 56,108 59,124 62,115 65,118 68,100 71,112 74,106 77,114 80,96 83,104 86,92 89,108 92,88 95,100 98,80 101,96 104,84 107,94 110,60 113,90 116,72 119,92 122,50 125,85 128,70 131,88 134,75 137,90 140,78 143,86 146,80 150,88 155,82 160,86"/>
      <polyline fill="none" stroke="var(--orange)" stroke-width=".8" points="160,86 185,78 205,72 215,65 225,66 230,58 240,56 245,48 255,44 260,38 270,34 275,28 285,24 290,18 296,14"/>
      <polyline fill="none" stroke="var(--line-grey)" stroke-width=".8" points="160,86 195,110 230,122 260,130 296,140"/>
      <polyline fill="none" stroke="var(--line-blue)" stroke-width=".8" points="160,86 170,98 176,94 184,106 190,102 198,112 206,108 214,118 222,114 230,122 238,118 248,126 256,124 266,130 276,128 286,136 296,138"/>
      <g><text x="40" y="156">1995</text><text x="64" y="156">2000</text><text x="88" y="156">2005</text><text x="112" y="156">2010</text><text x="136" y="156">2015</text><text x="160" y="156">2020</text><text x="184" y="156">2025</text><text x="208" y="156">2030</text><text x="232" y="156">2035</text><text x="256" y="156">2040</text><text x="280" y="156">2045</text></g>
      <line x1="90" y1="165" x2="98" y2="165" stroke="var(--orange)"/><text x="100" y="167">Average</text>
      <line x1="135" y1="165" x2="143" y2="165" stroke="var(--line-grey)"/><text x="145" y="167">Goals</text>
      <line x1="175" y1="165" x2="183" y2="165" stroke="var(--line-blue)"/><text x="185" y="167">With measure</text>
    </svg>
  </div>
  <div class="timeline">
    <div class="controls"><span>«</span><span class="play">▶</span><span>»</span></div>
    <svg class="axis" width="841" height="40">
      <defs><pattern id="tk4" width="6" height="6" patternUnits="userSpaceOnUse"><line x1="0.5" y1="0" x2="0.5" y2="6" stroke="#555" stroke-width=".6"/></pattern></defs>
      <line x1="116" y1="31" x2="841" y2="31" stroke="#333"/>
      <rect x="116" y="25" width="725" height="6" fill="url(#tk4)"/>
    </svg>
    <span class="tl-label" style="left:173px">January 2023</span><span class="tl-label" style="left:288px">July 2023</span><span class="tl-label" style="left:420px">January 2023</span><span class="tl-label" style="left:536px">July 2023</span><span class="tl-label" style="left:658px">January 2023</span><span class="tl-label" style="left:783px">July 2023</span>
    <div class="row" style="top:74px;height:31px"></div>
    <div class="row" style="top:109px;height:31px"></div>
    <div class="row" style="top:142px;height:31px"></div>
    <div class="row" style="top:176px;height:31px"></div>
    <div class="bar" style="left:174px;top:74px;width:195px;height:31px;background:var(--bar-teal)">Compressor rebundling<small>100 assets included</small><span class="info">i</span></div>
    <div class="bar" style="left:416px;top:109px;width:194px;height:31px;background:var(--bar-rose)">Optimize gas lift<small>100 assets included</small><span class="info">i</span></div>
    <div class="bar" style="left:174px;top:142px;width:195px;height:31px;background:var(--bar-gold)">Power from shore<small>100 assets included</small><span class="info">i</span></div>
    <div class="bar" style="left:174px;top:176px;width:195px;height:31px;background:var(--bar-slate)">Reduced flaring<small>100 assets included</small><span class="info">i</span></div>
    <div class="cursor now" style="left:172px;height:260px"></div>
    <svg class="mini" width="841" height="63">
      <rect x="241" y="0" width="247" height="63" fill="var(--band)"/>
      <path d="M0,47 L40,44 L80,45 L120,40 L160,43 L200,38 L241,41 L260,30 L280,34 L300,28 L330,33 L360,27 L390,32 L420,28 L450,31 L488,36 L530,44 L570,40 L610,44 L650,39 L690,43 L730,38 L770,42 L810,40 L841,42 L841,63 L0,63Z" fill="var(--area)"/>
    </svg>
  </div>
</section>

<!-- ===== Screen 5 ===== -->
<section class="screen" style="top:2924px">
  <nav class="sidebar">
    <div class="brand">BRELMONT<i></i></div>
    <div class="nav-item" style="top:63px">Switch Energy Carrier</div>
    <div class="nav-item group" style="top:90px">Energy Efficiency Measures</div>
    <div class="nav-sub" style="top:124px">Switch Energy Carrier</div>
    <div class="nav-sub" style="top:147px">Energy Efficiency Measures</div>
    <div class="nav-sub" style="top:170px">Venting To Flare</div>
    <div class="nav-sub" style="top:194px">Venting To Production</div>
    <div class="nav-sub" style="top:217px">Fugitive Emissions Measure</div>
    <div class="nav-sub" style="top:240px">Compressor Replacement</div>
    <div class="nav-sub" style="top:264px">Reduced Water Injection</div>
    <div class="nav-sub" style="top:287px">Drilling Improvements</div>
    <div class="nav-item group" style="top:319px">Ending Of Pipe Measures</div>
    <div class="nav-item group" style="top:345px">Company Structure</div>
    <div class="nav-sub" style="top:374px">Change End Of Life</div>
    <div class="nav-sub" style="top:400px">New Net Zero Assets</div>
    <div class="nav-sub" style="top:426px">Update License OwnerShips</div>
  </nav>
  <div class="card measure">
    <div class="dt-title">Power From Shore</div>
    <div class="dt-h" style="left:103px">Assets</div><div class="dt-h" style="left:305px">Prameters</div>
    <div class="filters"><b>Active filters</b><span class="pill">Lorem ipsum</span><span class="pill">Lorem ipsum</span><span class="pill">Lorem ipsum</span></div>
    <table class="assets">
      <tr><td>Lorem Ipsum</td><td>Lorem</td><td>Lorem</td><td>Lorem Ipsum</td><td>100%</td><td>Lorem</td></tr>
      <tr><td>Lorem Ipsum</td><td>Lorem</td><td>Lorem</td><td>Lorem Ipsum</td><td>100%</td><td>Lorem</td></tr>
      <tr><td>Lorem Ipsum</td><td>Lorem</td><td>Lorem</td><td>Lorem Ipsum</td><td>100%</td><td>Lorem</td></tr>
      <tr><td>Lorem Ipsum</td><td>Lorem</td><td>Lorem</td><td>Lorem Ipsum</td><td>100%</td><td>Lorem</td></tr>
      <tr><td>Lorem Ipsum</td><td>Lorem</td><td>Lorem</td><td>Lorem Ipsum</td><td>100%</td><td>Lorem</td></tr>
      <tr><td>Lorem Ipsum</td><td>Lorem</td><td>Lorem</td><td>Lorem Ipsum</td><td>100%</td><td>Lorem</td></tr>
      <tr><td>Lorem Ipsum</td><td>Lorem</td><td>Lorem</td><td>Lorem Ipsum</td><td>100%</td><td>Lorem</td></tr>
    </table>
    <div class="params">
      <div><span>Start</span><span class="pv">January 2023</span></div>
      <div><span>End</span><span class="pv">October 2024</span></div>
      <div><span>Duration</span><span class="pv">21 Months</span></div>
      <div><span>Factor</span><span class="pv">2x</span></div>
      <div><span>Jalla Jalla</span><span class="pv">2x</span></div>
    </div>
  </div>
  <div class="card chart-card">
    <div class="chart-title">Predicted Specific CO2 Emissions</div><div class="chart-dot"></div>
    <svg width="320" height="170" viewBox="0 0 320 170" font-size="4.5" fill="#888">
      <rect x="40" y="5" width="120" height="140" fill="var(--shade)"/>
      <g><text x="22" y="8">175</text><text x="22" y="28">150</text><text x="22" y="48">125</text><text x="22" y="68">100</text><text x="26" y="88">75</text><text x="26" y="108">50</text><text x="26" y="128">25</text><text x="30" y="146">0</text></g>
      <polyline fill="none" stroke="var(--orange)" stroke-width="1" points="40,125 44,112 47,128 50,118 53,122 56,108 59,124 62,115 65,118 68,100 71,112 74,106 77,114 80,96 83,104 86,92 89,108 92,88 95,100 98,80 101,96 104,84 107,94 110,60 113,90 116,72 119,92 122,50 125,85 128,70 131,88 134,75 137,90 140,78 143,86 146,80 150,88 155,82 160,86"/>
      <polyline fill="none" stroke="var(--orange)" stroke-width=".8" points="160,86 185,78 205,72 215,65 225,66 230,58 240,56 245,48 255,44 260,38 270,34 275,28 285,24 290,18 296,14"/>
      <polyline fill="none" stroke="var(--line-grey)" stroke-width=".8" points="160,86 195,110 230,122 260,130 296,140"/>
      <polyline fill="none" stroke="var(--line-blue)" stroke-width=".8" points="160,86 170,98 176,94 184,106 190,102 198,112 206,108 214,118 222,114 230,122 238,118 248,126 256,124 266,130 276,128 286,136 296,138"/>
      <g><text x="40" y="156">1995</text><text x="64" y="156">2000</text><text x="88" y="156">2005</text><text x="112" y="156">2010</text><text x="136" y="156">2015</text><text x="160" y="156">2020</text><text x="184" y="156">2025</text><text x="208" y="156">2030</text><text x="232" y="156">2035</text><text x="256" y="156">2040</text><text x="280" y="156">2045</text></g>
      <line x1="90" y1="165" x2="98" y2="165" stroke="var(--orange)"/><text x="100" y="167">Average</text>
      <line x1="135" y1="165" x2="143" y2="165" stroke="var(--line-grey)"/><text x="145" y="167">Goals</text>
      <line x1="175" y1="165" x2="183" y2="165" stroke="var(--line-blue)"/><text x="185" y="167">With measure</text>
    </svg>
  </div>
  <div class="timeline">
    <div class="controls"><span>«</span><span class="play">▶</span><span>»</span></div>
    <svg class="axis" width="841" height="40">
      <defs><pattern id="tk5" width="6" height="6" patternUnits="userSpaceOnUse"><line x1="0.5" y1="0" x2="0.5" y2="6" stroke="#555" stroke-width=".6"/></pattern></defs>
      <line x1="116" y1="31" x2="841" y2="31" stroke="#333"/>
      <rect x="116" y="25" width="725" height="6" fill="url(#tk5)"/>
    </svg>
    <span class="tl-label" style="left:173px">January 2023</span><span class="tl-label" style="left:288px">July 2023</span><span class="tl-label" style="left:420px">January 2023</span><span class="tl-label" style="left:536px">July 2023</span><span class="tl-label" style="left:658px">January 2023</span><span class="tl-label" style="left:783px">July 2023</span>
    <div class="row" style="top:54px;height:25px;right:0"></div>
    <div class="row" style="top:84px;height:25px;right:0"></div>
    <div class="row" style="top:114px;height:25px;right:0"></div>
    <div class="row" style="top:144px;height:25px;right:0"></div>
    <div class="row" style="top:174px;height:25px;right:0"></div>
    <div class="row" style="top:204px;height:25px;right:0"></div>
    <div class="row" style="top:234px;height:25px;right:0"></div>
    <div class="field" style="left:387px;top:54px;width:345px;background:var(--bar-slate)">Demo field 1</div>
    <div class="field" style="left:260px;top:84px;width:283px;background:var(--bar-rose)">Demo field 2</div>
    <div class="field" style="left:260px;top:114px;width:283px;background:var(--bar-gold)">Demo field 3</div>
    <div class="field" style="left:326px;top:144px;width:352px;background:var(--bar-lilac)">Demo field 4</div>
    <div class="field" style="left:241px;top:174px;width:268px;background:var(--bar-brown)">Demo field 5</div>
    <div class="field" style="left:375px;top:204px;width:342px;background:var(--bar-slate)">Demo field 6</div>
    <div class="field" style="left:375px;top:234px;width:342px;background:var(--bar-grey)">Demo field 7</div>
    <div class="cursor now" style="left:172px;height:260px"></div>
    <svg class="mini" width="841" height="63">
      <rect x="241" y="0" width="247" height="63" fill="var(--band)"/>
      <path d="M0,47 L40,44 L80,45 L120,40 L160,43 L200,38 L241,41 L260,30 L280,34 L300,28 L330,33 L360,27 L390,32 L420,28 L450,31 L488,36 L530,44 L570,40 L610,44 L650,39 L690,43 L730,38 L770,42 L810,40 L841,42 L841,63 L0,63Z" fill="var(--area)"/>
    </svg>
  </div>
</section>

</body>
</html>
```